Graphic to show our studio's values

We'd like to create a graphic of our values that can go onto fun gifts for our team in order to keep our values in front of all of us in a creative way. The graphic might go onto mugs, gift boxes, tote bags, etc. We are a growing interior architecture/design studio in Austin, TX. I encourage you to check out our website at www.vorrelandesign.com to get a sense of our vibe and culture. The graphic may or may not include the subtext to each value depending on how difficult it is to incorporate the subtext into a great design.

```html
<!DOCTYPE html>
<html lang="en">
<head>
<meta charset="utf-8">
<title>We Are — Studio Values</title>
<link rel="stylesheet" href="https://fonts.googleapis.com/css2?family=Playfair+Display:wght@700;900&family=Roboto:wght@400&display=swap">
<style>
  :root {
    --backdrop: #c4c2c7;
    --paper: #ebebed;
    --ink: #1c1b1e;
    --learners: #8cc04d;
    --positive: #e95a35;
    --trustworthy: #2f3190;
    --responsive: #bf2433;
  }
  html, body {
    margin: 0;
    padding: 0;
    width: 1135px;
    height: 1200px;
    overflow: hidden;
    background: var(--backdrop);
  }
  .poster {
    position: absolute;
    left: 246px;
    top: 183px;
    width: 630px;
    height: 830px;
    background: var(--paper);
    overflow: hidden;
  }
  .poster__title {
    position: absolute;
    left: -24px;
    bottom: 38px;
    margin: 0;
    writing-mode: vertical-rl;
    transform: rotate(180deg);
    font-family: "Playfair Display", serif;
    font-weight: 900;
    font-size: 240px;
    line-height: 1;
    color: var(--ink);
    white-space: nowrap;
  }
  .value {
    position: absolute;
    right: 56px;
    width: 380px;
    text-align: right;
  }
  .value--learners { top: 46px; }
  .value--positive { top: 244px; }
  .value--trustworthy { top: 444px; }
  .value--responsive { top: 629px; }
  .value__name {
    margin: 0;
    font-family: "Playfair Display", serif;
    font-weight: 700;
    font-size: 58px;
    line-height: 1;
  }
  .value--learners .value__name { color: var(--learners); }
  .value--positive .value__name { color: var(--positive); }
  .value--trustworthy .value__name { color: var(--trustworthy); }
  .value--responsive .value__name { color: var(--responsive); }
  .value__text {
    margin: 8px 0 0;
    font-family: "Roboto", sans-serif;
    font-size: 16px;
    line-height: 20px;
    color: var(--ink);
  }
</style>
</head>
<body>
  <main class="poster">
    <h1 class="poster__title">we are</h1>

    <section class="value value--learners">
      <h2 class="value__name">learners</h2>
      <p class="value__text">We look for opportunities to learn from<br>every project and interaction, and we<br>share what we learn with each other</p>
    </section>

    <section class="value value--positive">
      <h2 class="value__name">positive</h2>
      <p class="value__text">We look for the good, roll with the<br>punches, have a sense of humor and<br>celebrate each other.</p>
    </section>

    <section class="value value--trustworthy">
      <h2 class="value__name">trustworthy</h2>
      <p class="value__text">We are our client's advocate and<br>trustworthy teammate.</p>
    </section>

    <section class="value value--responsive">
      <h2 class="value__name">responsive</h2>
      <p class="value__text">We respond to our clients quickly and<br>with enthusiasm as engaged teammates<br>who are committed to partnering with<br>them in accomplishing their goals.</p>
    </section>
  </main>
</body>
</html>
```